Washington DC Solo Practitioner Law Firm needs Stationery and Business Card Design

We need a letterhead and business card for a new law firm based in Washington DC called Marlowe PLLC. The law firm is a single lawyer practicing appellate law (U.S. Supreme Court, Federal District Courts, State Supreme Courts).
We already have a logo designed through a PixelBazaar contest. The letterhead and the business card should include the Logo and have the same look and feel as the Logo - same fonts and colors, please. We would like a clean, crisp, simple, professional look. The design should convey stability and experience.
We have .png and .psd and .ai files for the logo, as needed
Dark blue color is PANTONE P 108-16 C
Grey color is PANTONE P 179-11 C
Type face is Century Gothic Regular typeface

```html
<!DOCTYPE html>
<html lang="en">
<head>
<meta charset="utf-8">
<title>Marlowe PLLC Stationery</title>
<link href="https://fonts.googleapis.com/css2?family=Questrial&display=swap" rel="stylesheet">
<style>
  :root {
    --navy: #06325f;
    --navy-soft: #1d4a7a;
    --grey-bg: #8c8c8c;
    --paper: #ffffff;
    --line-grey: #7a7a7a;
    --faint: #e9ecf1;
    --text-navy: #0a3464;
  }
  * { margin: 0; padding: 0; box-sizing: border-box; }
  html, body { width: 1200px; height: 1000px; overflow: hidden; }
  body {
    background: var(--grey-bg);
    font-family: "Questrial", "Century Gothic", sans-serif;
    position: relative;
  }
  .card, .letterhead {
    position: absolute;
    background: var(--paper);
    box-shadow: 2px 2px 3px rgba(0,0,0,.35);
    overflow: hidden;
  }
  .card { width: 325px; height: 191px; }
  .col-a { left: 19px; }
  .col-b { left: 367px; }
  .row-1 { top: 84px; }
  .row-2 { top: 302px; }
  .row-3 { top: 521px; }
  .row-4 { top: 751px; }
  .navy { background: var(--navy); }
  .block { position: absolute; background: var(--navy); }

  .wordmark { position: absolute; display: flex; align-items: center; gap: 14px; color: var(--navy); }
  .wordmark.light { color: #fff; }
  .wordmark .mark-square { background: currentColor; flex: none; }
  .wordmark .name { font-size: 28px; letter-spacing: 1px; line-height: 1; white-space: nowrap; }
  .wordmark .tagline { font-size: 9.5px; margin-top: 8px; white-space: nowrap; letter-spacing: .2px; }

  .holder { position: absolute; font-size: 16px; color: var(--text-navy); }
  .holder.light { color: #fff; }

  .contact { position: absolute; list-style: none; font-size: 11px; color: #555; line-height: 14.5px; }
  .contact.light { color: #fff; }
  .contact.navy-text { color: var(--text-navy); }
  .contact li { display: flex; align-items: flex-start; gap: 4px; }
  .contact svg { flex: none; margin-top: 1.5px; }
  .divider { position: absolute; width: 1px; background: currentColor; }

  .faint-square { position: absolute; }

  .label {
    position: absolute; left: 735px; top: 216px;
    color: #fff; font-size: 16px; line-height: 21px;
  }

  .letterhead { left: 713px; top: 342px; width: 464px; height: 601px; }
  .letterhead .top-rule { position: absolute; left: 0; top: 0; width: 100%; height: 4px; background: var(--navy); }
  .letterhead .footer {
    position: absolute; left: 0; bottom: 0; width: 100%; height: 40px;
    background: var(--navy); color: #fff; font-size: 7.5px; text-align: center; padding-top: 6px; line-height: 10px;
  }
  .letterhead .footer span { margin: 0 4px; }
</style>
</head>
<body>

<svg width="0" height="0" style="position:absolute">
  <defs>
    <symbol id="ico-phone" viewBox="0 0 10 10"><rect width="10" height="10" rx="1" fill="currentColor"/><path d="M3 2h1.4l.6 2-1 .7c.4 1 1.1 1.7 2 2l.7-1 2 .6V8c-3 .3-6-2.7-5.7-6z" fill="#fff"/></symbol>
    <symbol id="ico-mobile" viewBox="0 0 10 10"><rect width="10" height="10" rx="1" fill="currentColor"/><rect x="3.2" y="1.8" width="3.6" height="6.4" rx=".6" fill="#fff"/></symbol>
    <symbol id="ico-mail" viewBox="0 0 10 10"><rect width="10" height="10" rx="1" fill="currentColor"/><rect x="2" y="3" width="6" height="4.2" fill="#fff"/><path d="M2 3l3 2.4L8 3" stroke="currentColor" stroke-width=".7" fill="none"/></symbol>
    <symbol id="ico-pin" viewBox="0 0 10 10"><rect width="10" height="10" rx="1" fill="currentColor"/><path d="M5 1.8a2.3 2.3 0 0 1 2.3 2.3C7.3 5.8 5 8.3 5 8.3S2.7 5.8 2.7 4.1A2.3 2.3 0 0 1 5 1.8z" fill="#fff"/><circle cx="5" cy="4.1" r=".8" fill="currentColor"/></symbol>
  </defs>
</svg>

<!-- Option 1 -->
<section class="card col-a row-1">
  <div class="block" style="left:0;top:0;width:325px;height:86px"></div>
  <div class="faint-square" style="left:240px;top:8px;width:70px;height:70px;background:var(--navy-soft)"></div>
  <p class="holder light" style="left:116px;top:57px">Evan Marlowe</p>
  <ul class="contact" style="left:31px;top:117px;color:#555">
    <li><svg width="11" height="11" style="color:var(--navy)"><use href="#ico-phone"/></svg>202-555-0148</li>
    <li><svg width="11" height="11" style="color:var(--navy)"><use href="#ico-mobile"/></svg>571-555-0193</li>
    <li><svg width="11" height="11" style="color:var(--navy)"><use href="#ico-mail"/></svg>emarlowe@marlowepllc.com</li>
    <li><svg width="11" height="11" style="color:var(--navy)"><use href="#ico-pin"/></svg>1480 Carver Street NW, Suite 300, Washington, DC 20005</li>
  </ul>
</section>
<section class="card col-b row-1 navy">
  <div class="wordmark light" style="left:26px;top:62px">
    <span class="mark-square" style="width:56px;height:56px"></span>
    <div><div class="name">MARLOWE PLLC</div><div class="tagline">TRIAL AND APPELLATE LITIGATION</div></div>
  </div>
</section>

<!-- Option 2 -->
<section class="card col-a row-2">
  <div class="wordmark" style="left:78px;top:22px;gap:10px">
    <span class="mark-square" style="width:40px;height:40px"></span>
    <div><div class="name" style="font-size:21px">MARLOWE PLLC</div><div class="tagline" style="font-size:7px;margin-top:6px">TRIAL AND APPELLATE LITIGATION</div></div>
  </div>
  <div class="block" style="left:0;top:91px;width:325px;height:100px"></div>
  <p class="holder light" style="left:32px;top:102px">Evan Marlowe</p>
  <div class="divider" style="left:135px;top:103px;height:71px;background:#fff"></div>
  <ul class="contact light" style="left:145px;top:103px">
    <li><svg width="11" height="11" style="color:#fff"><use href="#ico-phone"/></svg>202-555-0148</li>
    <li><svg width="11" height="11" style="color:#fff"><use href="#ico-mobile"/></svg>571-555-0193</li>
    <li><svg width="11" height="11" style="color:#fff"><use href="#ico-mail"/></svg>emarlowe@marlowepllc.com</li>
    <li><svg width="11" height="11" style="color:#fff"><use href="#ico-pin"/></svg><span>1480 Carver Street NW, Suite 300<br>Washington, DC 20005</span></li>
  </ul>
</section>
<section class="card col-b row-2">
  <div class="wordmark" style="left:28px;top:62px">
    <span class="mark-square" style="width:56px;height:56px"></span>
    <div><div class="name">MARLOWE PLLC</div><div class="tagline">TRIAL AND APPELLATE LITIGATION</div></div>
  </div>
</section>

<!-- Option 3 -->
<section class="card col-a row-3">
  <div class="block" style="left:0;top:0;width:128px;height:191px"></div>
  <div class="faint-square" style="left:22px;top:52px;width:80px;height:80px;background:var(--navy-soft)"></div>
  <p class="holder" style="left:200px;top:17px">Evan Marlowe</p>
  <ul class="contact" style="left:144px;top:107px;color:#555">
    <li><svg width="11" height="11" style="color:var(--navy)"><use href="#ico-phone"/></svg>202-555-0148</li>
    <li><svg width="11" height="11" style="color:var(--navy)"><use href="#ico-mobile"/></svg>571-555-0193</li>
    <li><svg width="11" height="11" style="color:var(--navy)"><use href="#ico-mail"/></svg>emarlowe@marlowepllc.com</li>
    <li><svg width="11" height="11" style="color:var(--navy)"><use href="#ico-pin"/></svg><span>1480 Carver Street NW, Suite 300<br>Washington, DC 20005</span></li>
  </ul>
</section>
<section class="card col-b row-3">
  <div class="block" style="left:273px;top:0;width:52px;height:191px"></div>
  <div class="wordmark" style="left:24px;top:62px;gap:10px">
    <span class="mark-square" style="width:48px;height:48px"></span>
    <div><div class="name" style="font-size:23px">MARLOWE PLLC</div><div class="tagline" style="font-size:8.5px">TRIAL AND APPELLATE LITIGATION</div></div>
  </div>
</section>

<!-- Option 4 -->
<section class="card col-a row-4">
  <div class="block" style="left:0;top:0;width:325px;height:84px"></div>
  <div class="wordmark light" style="left:78px;top:22px;gap:10px">
    <span class="mark-square" style="width:40px;height:40px"></span>
    <div><div class="name" style="font-size:21px">MARLOWE PLLC</div><div class="tagline" style="font-size:7px;margin-top:6px">TRIAL AND APPELLATE LITIGATION</div></div>
  </div>
  <div class="block" style="left:0;top:84px;width:325px;height:3px;background:var(--line-grey)"></div>
  <div class="block" style="left:0;top:90px;width:325px;height:2px"></div>
  <p class="holder" style="left:37px;top:106px">Evan Marlowe</p>
  <div class="divider" style="left:136px;top:106px;height:70px;background:var(--navy)"></div>
  <ul class="contact" style="left:145px;top:106px;color:#555">
    <li><svg width="11" height="11" style="color:var(--navy)"><use href="#ico-phone"/></svg>202-555-0148</li>
    <li><svg width="11" height="11" style="color:var(--navy)"><use href="#ico-mobile"/></svg>571-555-0193</li>
    <li><svg width="11" height="11" style="color:var(--navy)"><use href="#ico-mail"/></svg>emarlowe@marlowepllc.com</li>
    <li><svg width="11" height="11" style="color:var(--navy)"><use href="#ico-pin"/></svg><span>1480 Carver Street NW, Suite 300<br>Washington, DC 20005</span></li>
  </ul>
</section>
<section class="card col-b row-4">
  <div class="wordmark" style="left:28px;top:40px">
    <span class="mark-square" style="width:56px;height:56px"></span>
    <div><div class="name">MARLOWE PLLC</div><div class="tagline">TRIAL AND APPELLATE LITIGATION</div></div>
  </div>
  <div class="block" style="left:0;top:149px;width:325px;height:5px;background:var(--line-grey)"></div>
  <div class="block" style="left:0;top:157px;width:325px;height:34px"></div>
</section>

<div class="label">Stationery<br>Business card: 4 front 4 back options<br>Letterheead</div>

<!-- Letterhead -->
<section class="letterhead">
  <div class="top-rule"></div>
  <div class="wordmark" style="left:29px;top:24px;gap:10px">
    <span class="mark-square" style="width:44px;height:44px"></span>
    <div><div class="name" style="font-size:19px">MARLOWE PLLC</div><div class="tagline" style="font-size:7px;margin-top:6px">TRIAL AND APPELLATE LITIGATION</div></div>
  </div>
  <div class="faint-square" style="left:147px;top:238px;width:170px;height:170px;background:var(--faint)"></div>
  <div class="footer">
    <div><span>202-555-0148</span><span>571-555-0193</span><span>emarlowe@marlowepllc.com</span></div>
    <div>1480 Carver Street NW, Suite 300, Washington, DC 20005</div>
  </div>
</section>

</body>
</html>
```